We need a banner ad design for a company based in Brazil called "Zunaro" (http://www.zunaro-exemplo.com.br), which offers escort services for men. Our main strength and focus is helping people easily search for escorts using mobile devices, by being an mobile optimized repository of escorts which are crawled from many non-mobile optimized sites.

Target Market(s)

Men at all ages (above 18) looking for escorts

Industry/Entity Type

Escort

Requirements
Must have
• Size must be 468x60
The logo must be on white background
Nice to have
• The banner could have an eye-catching animation

The banner could have a small and quick animation showing the usage of the mobile application (like navigating through the application).
Should not have
• If animated then the text should not be split between frames.

```html
<!DOCTYPE html>
<html lang="pt-BR">
<head>
<meta charset="utf-8">
<title>Zunaro – Banner</title>
<link href="https://fonts.googleapis.com/css2?family=Exo+2:wght@600&display=swap" rel="stylesheet">
<style>
  :root {
    --leather-deep: #6e070b;
    --leather-mid: #b0141a;
    --leather-light: #d8262c;
    --text-light: #ffffff;
    --brand-red: #c8141b;
    --panel-white: #ffffff;
    --device-frame: #f1f1f2;
    --device-edge: #c9c9cc;
    --screen-dark: #2e1b12;
    --screen-warm: #9a6a4a;
  }
  html, body {
    margin: 0;
    padding: 0;
    overflow: hidden;
    background: #ffffff;
  }
  .banner {
    position: relative;
    width: 1200px;
    height: 154px;
    overflow: hidden;
    background:
      radial-gradient(ellipse at 55% 45%, var(--leather-light) 0%, var(--leather-mid) 55%, var(--leather-deep) 100%);
    font-family: "Exo 2", "Arial", sans-serif;
  }
  .hero-visual {
    position: absolute;
    left: -24px;
    top: 10px;
    width: 370px;
    height: 134px;
    border-radius: 26px;
    background:
      linear-gradient(90deg, var(--device-edge) 0%, var(--device-frame) 6%, var(--device-frame) 12%, var(--screen-dark) 18%, var(--screen-warm) 48%, var(--screen-dark) 80%, var(--device-frame) 88%, var(--device-edge) 100%);
    box-shadow: 0 3px 8px rgba(0,0,0,0.35);
  }
  .headline {
    position: absolute;
    left: 376px;
    top: 20px;
    margin: 0;
    color: var(--text-light);
    font-weight: 600;
    font-size: 35px;
    line-height: 38px;
    letter-spacing: 0.3px;
    text-transform: uppercase;
    white-space: nowrap;
    text-shadow: 0 2px 3px rgba(0,0,0,0.35);
  }
  .headline span { display: block; }
  .brand-panel {
    position: absolute;
    left: 886px;
    top: 15px;
    width: 314px;
    height: 124px;
    background: var(--panel-white);
    border-radius: 32px 0 0 32px;
    display: flex;
    align-items: center;
    justify-content: center;
    gap: 12px;
  }
  .brand-dot {
    width: 20px;
    height: 20px;
    border-radius: 50%;
    background: var(--brand-red);
  }
  .brand-name {
    color: var(--brand-red);
    font-weight: 600;
    font-size: 50px;
    line-height: 1;
  }
</style>
</head>
<body>
  <div class="banner">
    <div class="hero-visual" role="img" aria-label="Mão segurando um smartphone que exibe uma foto do catálogo de acompanhantes"></div>
    <h1 class="headline">
      <span>O maior catálogo de</span>
      <span>acompanhantes</span>
      <span>na palma da sua mão</span>
    </h1>
    <div class="brand-panel">
      <div class="brand-dot"></div>
      <div class="brand-name">Zunaro</div>
    </div>
  </div>
</body>
</html>
```